Dorsey K. Wendell Business Card

We need a business card for our company Dorsey K. Wendell Heating & Plumbing to be distributed to potential customers. It should follow the color scheme of our logo and have a modern upscale and masculine look.

The logo is attached and the info below should also be included:

5187 W. Cedar Brook Rd.
Ashgrove, OR 17545

Russell T. Wendell
(717) 592-0817
russelltwendell@fernmail.net
dorseykwendell.net
PA #093148

Industry/Entity Type

Business

Contact Information for Business Card

5187 W. Cedar Brook Rd.
Ashgrove, OR 17545

Russell T. Wendell
(717) 592-0817
russelltwendell@fernmail.net
dorseykwendell.net
PA #093148

Colors

Designer to choose colors to be used in the design.

Requirements
Must have
• Information above included

```html
<!DOCTYPE html>
<html lang="en">
<head>
<meta charset="utf-8">
<title>Dorsey K. Wendell Business Card</title>
<link rel="stylesheet" href="https://fonts.googleapis.com/css2?family=Open+Sans:wght@300;400;700&display=swap">
<style>
  :root {
    --backdrop: #3b2b23;
    --card-light: #ffffff;
    --card-dark: #0b1720;
    --ink: #1d1d1d;
    --ink-soft: #3c3c3c;
    --brand-blue: #1f4fff;
    --brand-green: #80f000;
    --band-green: #7fff00;
    --band-orange: #ef9800;
    --band-red: #ee4a00;
    --placeholder: #d8d8d8;
  }
  * { box-sizing: border-box; margin: 0; padding: 0; }
  html, body { width: 1200px; height: 1007px; overflow: hidden; }
  body { background: var(--backdrop); font-family: "Open Sans", sans-serif; position: relative; }

  .card { position: absolute; top: 62px; width: 519px; height: 882px; overflow: hidden; }
  .card--front { left: 55px; background: linear-gradient(135deg, #e9ecec 0%, #f7f8f8 30%, var(--card-light) 55%, #f9fafa 85%, #eef0f0 100%); }
  .card--back { left: 621px; background: var(--card-dark); }

  .color-bands { position: absolute; left: 0; right: 0; bottom: 0; height: 36px; display: flex; }
  .color-bands span { flex: 1; }
  .color-bands .green { background: var(--band-green); }
  .color-bands .orange { background: var(--band-orange); }
  .color-bands .red { background: var(--band-red); }

  .portrait-ring { position: absolute; left: 148px; top: 133px; width: 224px; height: 224px; border: 2px solid var(--brand-blue); border-radius: 50%; display: flex; align-items: center; justify-content: center; }
  .portrait { width: 208px; height: 208px; border-radius: 50%; background: radial-gradient(circle at 50% 40%, var(--placeholder), #5a5a5a); }

  .person-name { position: absolute; left: 0; right: 0; top: 386px; text-align: center; font-weight: 400; font-size: 37px; letter-spacing: 0.5px; color: var(--ink); }

  .contact-list { position: absolute; left: 63px; top: 535px; list-style: none; }
  .contact-item { display: flex; align-items: center; height: 60px; margin-bottom: 29px; }
  .contact-item:nth-child(2) { margin-bottom: 28px; }
  .contact-icon { width: 60px; height: 60px; flex: none; }
  .contact-text { margin-left: 23px; font-size: 25px; font-weight: 400; line-height: 32px; color: var(--ink-soft); }

  .brand-lockup { position: absolute; left: 73px; top: 395px; display: flex; align-items: center; }
  .brand-square { width: 84px; height: 84px; background: var(--brand-blue); flex: none; }
  .brand-name { margin-left: 14px; font-weight: 700; color: var(--brand-green); font-size: 27px; line-height: 32px; letter-spacing: 0.5px; text-transform: uppercase; }
  .brand-name small { display: block; font-size: 15px; line-height: 22px; letter-spacing: 1.5px; }

  .back-web { position: absolute; left: 0; right: 0; top: 777px; text-align: center; font-size: 22px; color: var(--brand-green); }
</style>
</head>
<body>
  <section class="card card--front">
    <div class="portrait-ring">
      <div class="portrait" role="img" aria-label="Portrait photo of Russell T. Wendell"></div>
    </div>
    <h1 class="person-name">RUSSELL T. WENDELL</h1>
    <ul class="contact-list">
      <li class="contact-item">
        <svg class="contact-icon" viewBox="0 0 60 60" aria-hidden="true">
          <circle cx="30" cy="30" r="28.5" fill="#fff" stroke="var(--brand-blue)" stroke-width="2"/>
          <path d="M17 26c0-4 6-6 13-6s13 2 13 6v2h-6v-3h-14v3h-6z" fill="var(--brand-blue)"/>
          <rect x="19" y="29" width="22" height="12" rx="2" fill="var(--brand-blue)"/>
          <g fill="#fff"><circle cx="26" cy="33" r="1"/><circle cx="30" cy="33" r="1"/><circle cx="34" cy="33" r="1"/><circle cx="26" cy="37" r="1"/><circle cx="30" cy="37" r="1"/><circle cx="34" cy="37" r="1"/></g>
        </svg>
        <p class="contact-text">(717) 592-0817</p>
      </li>
      <li class="contact-item">
        <svg class="contact-icon" viewBox="0 0 60 60" aria-hidden="true">
          <circle cx="30" cy="30" r="30" fill="var(--brand-blue)"/>
          <g fill="none" stroke="#fff" stroke-width="2">
            <circle cx="30" cy="30" r="13"/>
            <ellipse cx="30" cy="30" rx="6" ry="13"/>
            <line x1="17" y1="30" x2="43" y2="30"/>
            <line x1="30" y1="17" x2="30" y2="43"/>
            <path d="M19 23h22M19 37h22"/>
          </g>
        </svg>
        <p class="contact-text">russelltwendell@fernmail.net<br>www.dorseykwendell.net</p>
      </li>
      <li class="contact-item">
        <svg class="contact-icon" viewBox="0 0 60 60" aria-hidden="true">
          <circle cx="30" cy="30" r="28.5" fill="#fff" stroke="var(--brand-blue)" stroke-width="2"/>
          <g fill="none" stroke="var(--brand-blue)" stroke-width="1.6" stroke-linejoin="round">
            <path d="M18 30l12-11 12 11"/>
            <path d="M21 28v13h18V28"/>
            <path d="M27 41v-7h6v7"/>
          </g>
        </svg>
        <p class="contact-text">5187 W. Cedar Brook Rd.<br>Ashgrove, OR #093148</p>
      </li>
    </ul>
    <div class="color-bands"><span class="green"></span><span class="orange"></span><span class="red"></span></div>
  </section>

  <section class="card card--back">
    <div class="brand-lockup">
      <div class="brand-square"></div>
      <p class="brand-name">Dorsey K. Wendell<small>Heating &amp; Plumbing</small></p>
    </div>
    <p class="back-web">www.dorseykwendell.net</p>
    <div class="color-bands"><span class="green"></span><span class="orange"></span><span class="red"></span></div>
  </section>
</body>
</html>
```